Lumo -Fresh business card design

It is a dry cleaning carpet business.
Red wine stain removal and pet urine treatments.
Servicing all regional areas.
Updates

all logo and pictures files have been uploaded

Industry/Entity Type

Dry Cleaning

Contact Information for Business Card

Lumo-Fresh Carpet and upholstery cleaning.
Servicing Albury/Wodonga and surrounding areas.
ph gus 0461273904 ,email lumofresh1@tealpost.example

Font styles to use
Serif
Sans Serif
Other font styles liked:
• lumo fresh logo font

Colors
ec2027
ffcf3e
33a6d7
0692cd

Requirements
Nice to have
• I have included photos of the logo and car and stripe on van ,I dont need all of them in the card just i would like to stick to these colours.

```html
<!DOCTYPE html>
<html lang="en">
<head>
<meta charset="utf-8">
<title>Lumo-Fresh Business Card</title>
<link rel="stylesheet" href="https://fonts.googleapis.com/css2?family=Archivo+Black&family=Cinzel:wght@500&family=Montserrat:wght@500;700;800&display=swap">
<style>
  :root {
    --brand-blue: #3cb4e6;
    --label-blue: #33b6ea;
    --stripe-cyan: #3ad3e8;
    --stripe-yellow: #ffcf3e;
    --stripe-red: #ec2027;
    --icon-red: #ec2027;
    --icon-yellow: #ffc02e;
    --phone-pink: #f0457a;
    --ink: #111111;
    --paper: #ffffff;
  }
  * { margin: 0; padding: 0; box-sizing: border-box; }
  html, body { width: 1200px; height: 740px; overflow: hidden; background: var(--paper); }
  .card {
    position: relative;
    width: 1200px;
    height: 740px;
    background: var(--paper);
    overflow: hidden;
    font-family: "Montserrat", Arial, sans-serif;
    color: var(--ink);
  }
  .card__stripes { position: absolute; inset: 0; width: 1200px; height: 740px; }
  .brand-name {
    position: absolute;
    left: 66px;
    top: 40px;
    font-family: "Archivo Black", Arial, sans-serif;
    font-size: 100px;
    line-height: 1;
    letter-spacing: 1px;
    color: var(--brand-blue);
  }
  .tagline {
    position: absolute;
    left: 70px;
    top: 200px;
    font-weight: 800;
    font-size: 32px;
    letter-spacing: 0.5px;
  }
  .contact {
    position: absolute;
    left: 70px;
    display: flex;
    align-items: center;
    gap: 28px;
    font-size: 26px;
    letter-spacing: 3px;
  }
  .contact--phone { top: 258px; font-weight: 700; }
  .contact--email { top: 306px; font-weight: 500; }
  .contact__icon { width: 34px; height: 34px; flex: none; }
  .contact__at {
    width: 34px;
    text-align: center;
    color: var(--icon-red);
    font-weight: 800;
    font-size: 30px;
    letter-spacing: 0;
  }
  .service {
    position: absolute;
    top: 408px;
    width: 240px;
    display: flex;
    flex-direction: column;
    align-items: center;
  }
  .service--stain { left: 34px; }
  .service--pet { left: 284px; }
  .service--dry { left: 548px; }
  .service__art { height: 110px; border-radius: 10px; }
  .service--stain .service__art { width: 126px; background: var(--icon-red); border-radius: 50%; }
  .service--pet .service__art { width: 132px; background: var(--icon-yellow); }
  .service--dry .service__art { width: 144px; background: var(--icon-red); }
  .service__label {
    margin-top: 12px;
    font-family: "Archivo Black", Arial, sans-serif;
    font-size: 25px;
    line-height: 27px;
    text-align: center;
    color: var(--label-blue);
    white-space: nowrap;
  }
  .service-area {
    position: absolute;
    left: 70px;
    top: 638px;
    font-family: "Cinzel", "Times New Roman", serif;
    font-weight: 500;
    font-size: 20px;
    letter-spacing: 1px;
  }
</style>
</head>
<body>
<main class="card">
  <svg class="card__stripes" viewBox="0 0 1200 740" aria-hidden="true">
    <polygon points="750,740 1200,96 1200,230 840,740" fill="var(--stripe-cyan)"/>
    <polygon points="840,740 1200,230 1200,262 862,740" fill="var(--stripe-yellow)"/>
    <polygon points="862,740 1200,262 1200,740" fill="var(--stripe-red)"/>
  </svg>

  <h1 class="brand-name">LUMO-FRESH</h1>
  <p class="tagline">CARPET AND UPHOLSTERY CLEANING</p>

  <p class="contact contact--phone">
    <svg class="contact__icon" viewBox="0 0 34 34" aria-hidden="true">
      <rect width="34" height="34" rx="7" fill="var(--phone-pink)"/>
      <path d="M11 8c1.5-1 3 1.5 3.6 3 .4 1-.6 1.8-1.2 2.4.8 2.6 3.2 5 5.8 5.8.6-.6 1.4-1.6 2.4-1.2 1.5.6 4 2.1 3 3.6-1 1.6-2.4 2.6-4.4 2.2C13.5 22.5 9.5 18.5 8.2 12.3 7.8 10.4 9.4 9 11 8z" fill="#fff"/>
    </svg>
    <span>gus 0461273904</span>
  </p>
  <p class="contact contact--email">
    <span class="contact__at" aria-hidden="true">@</span>
    <span>lumofresh1@tealpost.example</span>
  </p>

  <div class="service service--stain">
    <div class="service__art" role="img" aria-label="Red splash illustration"></div>
    <p class="service__label">RED STAIN<br>REMOVAL</p>
  </div>
  <div class="service service--pet">
    <div class="service__art" role="img" aria-label="Yellow dog and cat silhouette illustration"></div>
    <p class="service__label">PET URINE<br>TREATMENT</p>
  </div>
  <div class="service service--dry">
    <div class="service__art" role="img" aria-label="Red silhouette of a worker cleaning carpet"></div>
    <p class="service__label">DRY CLEANING<br>CARPETS</p>
  </div>

  <p class="service-area">SERVICING ALBURY/WODONGA AND SURROUNDING AREAS</p>
</main>
</body>
</html>
```